Eye Doctor Needs Updated Business Card

We need a standard US business card designed for an optometrist's practice. Our practice name is Halvorn Vision Center and attached you'll find our logos. We are located in a smaller community, we are a trusted source for eye care and designer eyewear. We have 2 different version of our logos, so both versions are attached. Our slogan is "Small Town Values, World Class Care". I'd like to see designs with one of our logos on the front with our contact info, and have the slogan on the back by itself. Final design should be professional looking, include the colors of our logo or colors that compliment the logo. We want it to look appropriate for a healthcare practice but also up-to-date, eye-catching, to have the normal contact info like address, phone #, email, but also possibly room for additional contact info such as facebook.
Updates

I just uploaded .eps files to use instead of the jpeg. Hope that helps!

So many great designs! We tending to like the darker blues that are used in our logo as the main blue color for the business cards. We also really like the use of a water-mark type appearance on either the front and/or back, or the embossed look as well looks nice. Thank you all for such great designs!

We're preferring the designs where white and the darker blue used in our logo are the primary colors on the front, but with a little green used as well. Again though, thanks for all the impressive designs so far!

Industry/Entity Type

Healthcare

```html
<!DOCTYPE html>
<html lang="en">
<head>
<meta charset="utf-8">
<title>Halvorn Vision Center — Business Card</title>
<link rel="stylesheet" href="https://fonts.googleapis.com/css2?family=Cormorant+Garamond:wght@500;600&display=swap">
<style>
  :root {
    --backdrop: #5b6475;
    --card-grey: #a9a9ab;
    --band-light: #cfcfd1;
    --brand-green: #3da93a;
    --brand-blue: #1a2f7a;
    --text-light: #ececec;
    --shadow: rgba(20, 24, 35, 0.35);
  }
  * { box-sizing: border-box; margin: 0; padding: 0; }
  html, body { width: 1200px; height: 1000px; overflow: hidden; }
  body {
    background: var(--backdrop);
    font-family: "Cormorant Garamond", Georgia, serif;
    position: relative;
  }
  .card {
    position: absolute;
    left: 250px;
    width: 700px;
    height: 400px;
    background: var(--card-grey);
    box-shadow: 0 10px 24px var(--shadow);
    overflow: hidden;
  }
  .card--back { top: 60px; }
  .card--front { top: 540px; }

  .stripe { position: absolute; left: 0; }
  .card--back .stripe--green { top: 0; width: 70px; height: 110px; background: var(--brand-green); }
  .card--back .stripe--blue { top: 110px; width: 70px; height: 170px; background: var(--brand-blue); }

  .card--front .band-top { position: absolute; left: 0; top: 0; width: 100%; height: 52px; background: var(--band-light); }
  .card--front .stripe--green { top: 52px; width: 70px; height: 118px; background: var(--brand-green); }
  .card--front .stripe--blue { top: 170px; width: 70px; height: 230px; background: var(--brand-blue); }

  .brand {
    position: absolute;
    display: flex;
    align-items: center;
    gap: 12px;
    color: var(--brand-blue);
    font-weight: 600;
    font-size: 24px;
    letter-spacing: 0.04em;
    white-space: nowrap;
  }
  .brand__dot {
    width: 26px; height: 26px; border-radius: 50%;
    background: var(--brand-green);
    flex: none;
  }
  .card--back .brand { top: 34px; left: 260px; }
  .card--front .brand { bottom: 40px; left: 120px; }

  .tagline {
    position: absolute;
    left: 130px;
    bottom: 70px;
    color: var(--text-light);
    font-weight: 500;
    font-size: 58px;
    letter-spacing: 0.01em;
  }

  .contact {
    position: absolute;
    right: 70px;
    top: 120px;
    color: var(--text-light);
    text-align: left;
    font-weight: 500;
  }
  .contact__name { font-size: 40px; margin-bottom: 34px; }
  .contact__line { font-size: 22px; line-height: 1.25; }
</style>
</head>
<body>
  <section class="card card--back" aria-label="Card back">
    <div class="stripe stripe--green"></div>
    <div class="stripe stripe--blue"></div>
    <div class="brand"><span class="brand__dot"></span>Halvorn Vision Center</div>
    <p class="tagline">Your Sample Text Logo</p>
  </section>

  <section class="card card--front" aria-label="Card front">
    <div class="band-top"></div>
    <div class="stripe stripe--green"></div>
    <div class="stripe stripe--blue"></div>
    <div class="contact">
      <p class="contact__name">Employee Name</p>
      <p class="contact__line">Mobile 0000 000 000</p>
      <p class="contact__line">email: yourmail@mail.com</p>
      <p class="contact__line">sitenamel.com.usa</p>
    </div>
    <div class="brand"><span class="brand__dot"></span>Halvorn Vision Center</div>
  </section>
</body>
</html>
```